Onboarding Infographic/brochure

We are a small criminal defense firm looking to create some sort of infographic or brochure that we can onboard new clients with. We are currently sending it out via email but want something a bit cooler and fun to send to clients. The information is:

A Few Quick Rules

We are here to help each step of the way. While questions are never discouraged, this letter will answer some of the most common ones we get asked.

Communications

As a client, you should always be in the loop. While we will try to respond to questions as quickly as possible, sometimes we are unable to respond right away. Do not worry - we promise to get back to you soon. Some questions might take some time to research, and a correct answer is better than a quick one.

Appointments

One of the benefits of having an attorney is the ability to discuss your case outside of court, minus the stress and headaches. If you need an appointment, please contact the office.

Appointments must be scheduled in advance. We do not want you to make a special trip to the office only to learn that we are in court or otherwise unavailable.

Jail Visits

If your family member is currently in jail, we take that very seriously. We will visit your loved one and introduce ourselves. While the case is ongoing, we ask that a family member be designated a “contact” person so that messages can be relayed quickly. Never discuss the facts of the case over the phone with someone who is in jail. Jail calls are recorded and we have seen too many cases go south based on remarks made over recorded lines.

Police Reports and Discovery

We will do our best to provide you with copies of everything we receive on your case. Most information will be emailed, so please keep your email address up to date.

Changes in Contact Information

If you move or change numbers during the case, please let us know. It is difficult to help if we are unable to reach you, and helping you is why we are here.

Court Appearances

Cases do not get resolved as quickly as they do on television. Expect there to be several hearings in your case and it may be necessary for you to attend one or more of them. If a hearing is set, you will receive notice of the date and time of each hearing.

Billing and Collections

We understand that this investment was a huge decision for you. As we focus on providing the best representation, we will need for you to stay on schedule with any payment arrangements agreed to at the time of your initial consultation.

Again, thank you for your trust in us. We look forward to getting a fantastic outcome on your case.

Target Market(s)

Criminal defense clients and their families

Industry/Entity Type

Legal

Font styles to use
Serif

Requirements
Must have
• Must incorporate all of the rules we email out. Would like diagrams, images or pictures
Nice to have
• We attached a Welcome brochure. Not sure I want it to look super similar, hence the request for infographic.

```html
<!DOCTYPE html>
<html lang="en">
<head>
<meta charset="utf-8">
<title>Norwell Legal Group – A Few Quick Rules</title>
<link rel="stylesheet" href="https://fonts.googleapis.com/css2?family=Rubik:ital,wght@0,500;0,700;0,800;1,500;1,700&family=Manrope:wght@400;500;700;800&display=swap">
<style>
  :root {
    --backdrop: #cbbfa7;
    --navy: #152b50;
    --paper: #ededed;
    --ink: #1d2333;
    --gold: #c9a54e;
    --teal: #4a9485;
    --maroon: #621f32;
    --blue: #3278b4;
    --green: #2a4d14;
    --orange: #cc5a3f;
    --brown: #8a6048;
    --white: #ffffff;
  }
  * { margin: 0; padding: 0; box-sizing: border-box; }
  html, body { width: 787px; height: 1200px; overflow: hidden; }
  body { background: var(--backdrop); font-family: "Manrope", sans-serif; color: var(--ink); }

  .brochure {
    position: absolute; left: 98px; top: 73px;
    display: grid;
    grid-template-columns: 284px 284px;
    grid-template-rows: repeat(5, 200px);
    column-gap: 24px; row-gap: 13.3px;
  }
  .panel { position: relative; overflow: hidden; background: var(--paper); }

  /* Cover */
  .cover { background: var(--navy); color: var(--white); }
  .cover-art { position: absolute; inset: 0; }
  .brand { position: absolute; left: 19px; top: 15px; font-family: "Rubik", sans-serif; color: var(--white); }
  .brand-name { font-size: 15px; font-weight: 800; letter-spacing: 0.3px; line-height: 1; }
  .brand-tag { font-size: 4.6px; font-weight: 800; letter-spacing: 3.2px; margin-top: 1px; }
  .cover-intro { position: absolute; left: 19px; top: 98px; padding-left: 8px; border-left: 2.5px solid var(--teal); width: 215px; }
  .cover-title { font-family: "Rubik", sans-serif; font-weight: 700; font-size: 14.4px; color: var(--gold); line-height: 1.1; }
  .cover-text { font-family: "Rubik", sans-serif; font-style: italic; font-weight: 500; font-size: 8.6px; line-height: 11.3px; margin-top: 3px; width: 180px; }
  .cover-text strong { font-weight: 700; }
  .cover-arrow { position: absolute; left: 243px; top: 183px; }

  /* Index */
  .index-art { position: absolute; inset: 0; }
  .index-list { position: absolute; left: 36px; top: 49px; list-style: none; }
  .index-list li { display: flex; align-items: center; height: 16.7px; font-size: 8px; color: #2a3042; }
  .index-num { width: 9px; height: 9px; border-radius: 50%; color: var(--white); font-size: 6px; display: inline-flex; align-items: center; justify-content: center; margin-right: 6px; }
  .index-list svg { margin-left: 3px; }

  /* Section panels */
  .section-head { height: 46px; border-bottom: 2.2px solid var(--navy); display: flex; align-items: center; justify-content: space-between; padding: 0 17px; color: var(--white); }
  .section-title { font-family: "Rubik", sans-serif; font-weight: 800; font-size: 14px; letter-spacing: 0.1px; }
  .section-icon { width: 32px; height: 32px; opacity: 0.75; }
  .section-text { position: absolute; left: 17px; top: 58px; width: 122px; font-size: 7.3px; line-height: 10.5px; }
  .section-text strong { font-weight: 800; }
  .section-text p + p { margin-top: 4px; }
  .photo { position: absolute; left: 146px; top: 60px; width: 122px; height: 98px; border-radius: 7px; box-shadow: 2px 2px 0 var(--navy); }
  .rule { position: absolute; left: 17px; right: 17px; bottom: 11px; height: 1px; }

  .communications .section-head { background: var(--gold); }
  .communications .rule { background: var(--gold); }
  .appointments .section-head, .billing .section-head { background: var(--teal); }
  .appointments .rule, .billing .rule { background: var(--teal); }
  .jail .section-head { background: var(--maroon); }
  .jail .rule { background: var(--maroon); }
  .jail .section-text { line-height: 9.6px; width: 124px; }
  .discovery .section-head { background: var(--blue); }
  .discovery .rule { background: var(--blue); }
  .contact-info .section-head { background: var(--green); }
  .contact-info .rule { background: var(--green); }
  .court .section-head { background: var(--orange); }
  .court .rule { background: var(--orange); }

  /* Closing */
  .closing { background: var(--navy); color: var(--white); text-align: center; }
  .quote-mark { position: absolute; left: 0; right: 0; font-family: "Rubik", sans-serif; font-weight: 800; color: var(--gold); font-size: 15px; line-height: 1; }
  .quote-text { position: absolute; left: 0; right: 0; top: 53px; font-family: "Rubik", sans-serif; font-style: italic; font-weight: 700; font-size: 9.6px; line-height: 14px; }
  .contacts { position: absolute; top: 148px; left: 0; right: 0; }
  .contact { position: absolute; transform: translateX(-50%); display: flex; flex-direction: column; align-items: center; font-size: 5.4px; font-weight: 800; white-space: nowrap; }
  .contact-dot { width: 12px; height: 12px; border-radius: 50%; background: var(--gold); display: flex; align-items: center; justify-content: center; margin-bottom: 6px; }
</style>
</head>
<body>
<main class="brochure">

  <section class="panel cover">
    <svg class="cover-art" width="284" height="200" viewBox="0 0 284 200">
      <defs>
        <clipPath id="coverCircle"><circle cx="237" cy="45" r="87"/></clipPath>
        <linearGradient id="handshakeTone" x1="0" y1="0" x2="1" y2="1">
          <stop offset="0" stop-color="#d9dadb"/><stop offset="0.55" stop-color="#8d8880"/><stop offset="1" stop-color="#3a3530"/>
        </linearGradient>
      </defs>
      <circle cx="235" cy="45" r="90" fill="var(--gold)"/>
      <g role="img" aria-label="Photo of a lawyer and client shaking hands over a desk with a gavel">
        <rect x="140" y="-50" width="200" height="190" fill="url(#handshakeTone)" clip-path="url(#coverCircle)"/>
      </g>
    </svg>
    <div class="brand">
      <div class="brand-name">NORWELL</div>
      <div class="brand-tag">LEGAL GROUP</div>
    </div>
    <div class="cover-intro">
      <h1 class="cover-title">A Few Quick Rules</h1>
      <p class="cover-text">We are here to help each step of the way. While questions are never discouraged, <strong>this letter will answer some of the most common ones we get asked.</strong></p>
    </div>
    <svg class="cover-arrow" width="25" height="6" viewBox="0 0 25 6"><path d="M0 3H23M20 0.8L23.5 3 20 5.2" fill="none" stroke="var(--teal)" stroke-width="0.9"/></svg>
  </section>

  <section class="panel index">
    <svg class="index-art" width="284" height="200" viewBox="0 0 284 200">
      <defs>
        <clipPath id="indexCircle"><circle cx="232" cy="20" r="84"/></clipPath>
        <radialGradient id="gavelTone" cx="0.6" cy="0.4" r="0.7">
          <stop offset="0" stop-color="#8a7760"/><stop offset="0.6" stop-color="#3d3026"/><stop offset="1" stop-color="#1e1915"/>
        </radialGradient>
      </defs>
      <circle cx="232" cy="20" r="87" fill="var(--navy)"/>
      <g role="img" aria-label="Photo of a wooden judge's gavel on its block">
        <rect x="140" y="-70" width="190" height="180" fill="url(#gavelTone)" clip-path="url(#indexCircle)"/>
      </g>
    </svg>
    <ol class="index-list">
      <li><span class="index-num" style="background:var(--gold)">1</span>Communications<svg width="9" height="5" viewBox="0 0 9 5"><path d="M0 2.5H8M6 0.8L8.3 2.5 6 4.2" fill="none" stroke="#2a3042" stroke-width="0.7"/></svg></li>
      <li><span class="index-num" style="background:var(--teal)">2</span>Appointments<svg width="9" height="5" viewBox="0 0 9 5"><path d="M0 2.5H8M6 0.8L8.3 2.5 6 4.2" fill="none" stroke="#2a3042" stroke-width="0.7"/></svg></li>
      <li><span class="index-num" style="background:var(--maroon)">3</span>Jail Visits<svg width="9" height="5" viewBox="0 0 9 5"><path d="M0 2.5H8M6 0.8L8.3 2.5 6 4.2" fill="none" stroke="#2a3042" stroke-width="0.7"/></svg></li>
      <li><span class="index-num" style="background:var(--blue)">4</span>Police Reports and Discovery<svg width="9" height="5" viewBox="0 0 9 5"><path d="M0 2.5H8M6 0.8L8.3 2.5 6 4.2" fill="none" stroke="#2a3042" stroke-width="0.7"/></svg></li>
      <li><span class="index-num" style="background:var(--green)">5</span>Changes in Contact Information<svg width="9" height="5" viewBox="0 0 9 5"><path d="M0 2.5H8M6 0.8L8.3 2.5 6 4.2" fill="none" stroke="#2a3042" stroke-width="0.7"/></svg></li>
      <li><span class="index-num" style="background:var(--orange)">6</span>Court Appearances<svg width="9" height="5" viewBox="0 0 9 5"><path d="M0 2.5H8M6 0.8L8.3 2.5 6 4.2" fill="none" stroke="#2a3042" stroke-width="0.7"/></svg></li>
      <li><span class="index-num" style="background:var(--brown)">7</span>Billing and Collections<svg width="9" height="5" viewBox="0 0 9 5"><path d="M0 2.5H8M6 0.8L8.3 2.5 6 4.2" fill="none" stroke="#2a3042" stroke-width="0.7"/></svg></li>
    </ol>
  </section>

  <section class="panel communications">
    <header class="section-head">
      <h2 class="section-title">Communications</h2>
      <svg class="section-icon" viewBox="0 0 32 32" fill="none" stroke="#fff" stroke-width="1"><path d="M13 6h14a3 3 0 0 1 3 3v7a3 3 0 0 1-3 3h-1v4l-4-4h-2"/><path d="M5 12h13a3 3 0 0 1 3 3v7a3 3 0 0 1-3 3H10l-5 4v-4a3 3 0 0 1-3-3v-7a3 3 0 0 1 3-3z"/><path d="M7 17h10M7 20h10M18 10h8"/></svg>
    </header>
    <div class="section-text">
      <p>As a client, you should always be in the loop. While we will try to respond to questions as quickly as possible, sometimes we are unable to respond right away. <strong>Do not worry - we promise to get back to you soon. Some questions might take some time to research, and a correct answer is better than a quick one.</strong></p>
    </div>
    <div class="photo" role="img" aria-label="Photo of an attorney in glasses talking with a client across a table" style="background:linear-gradient(135deg,#c9c3b8,#7b6a55 55%,#2c2f38)"></div>
    <div class="rule"></div>
  </section>

  <section class="panel appointments">
    <header class="section-head">
      <h2 class="section-title">Appointments</h2>
      <svg class="section-icon" viewBox="0 0 32 32" fill="none" stroke="#fff" stroke-width="1"><rect x="3" y="6" width="26" height="22" rx="2"/><path d="M3 11h26M9 3v5M23 3v5"/><circle cx="10" cy="16" r="1.5"/><circle cx="16" cy="16" r="1.5"/><circle cx="22" cy="16" r="1.5"/><circle cx="16" cy="22" r="1.5"/><circle cx="22" cy="22" r="1.5"/><circle cx="9" cy="23" r="3.5"/><path d="M7.5 23l1.2 1.2 2-2.2"/></svg>
    </header>
    <div class="section-text">
      <p>One of the benefits of having an attorney is the ability to discuss your case outside of court, minus the stress and headaches. If you need an appointment, please contact the office.</p>
      <p><strong>Appointments must be scheduled in advance. We do not want you to make a special trip to the office only to learn that we are in court or otherwise unavailable.</strong></p>
    </div>
    <div class="photo" role="img" aria-label="Photo of a lawyer meeting with two clients at a laptop" style="background:linear-gradient(135deg,#6d7a86,#2f3d55 50%,#8a7a6a)"></div>
    <div class="rule"></div>
  </section>

  <section class="panel jail">
    <header class="section-head">
      <h2 class="section-title">Jail Visits</h2>
      <svg class="section-icon" viewBox="0 0 32 32" fill="none" stroke="#fff" stroke-width="1"><rect x="2" y="3" width="28" height="26"/><path d="M2 6h28M2 26h28M7 6v20M12 6v20M20 6v20M25 6v20"/><circle cx="16" cy="14" r="3"/><path d="M11 26c0-5 2-7 5-7s5 2 5 7"/></svg>
    </header>
    <div class="section-text">
      <p>If your family member is currently in jail, we take that very seriously. We will visit your loved one and introduce ourselves. While the case is ongoing, we ask that a family member be designated a <strong>“contact” person so that messages can be relayed quickly.</strong> Never discuss the facts of the case over the phone with someone who is in jail. Jail calls are recorded and we have seen too many cases go south based on remarks made over recorded lines.</p>
    </div>
    <div class="photo" role="img" aria-label="Photo of an inmate in an orange uniform on a visitation phone facing a visitor" style="background:linear-gradient(120deg,#8a7a6c,#4b3f38 45%,#1c1a1a)"></div>
    <div class="rule"></div>
  </section>

  <section class="panel discovery">
    <header class="section-head">
      <h2 class="section-title">Police Reports and Discovery</h2>
      <svg class="section-icon" viewBox="0 0 32 32" fill="none" stroke="#fff" stroke-width="1"><rect x="5" y="4" width="22" height="26" rx="1.5"/><rect x="11" y="2" width="10" height="4" rx="1"/><path d="M16 9l5 2v3c0 3-2 5-5 6-3-1-5-3-5-6v-3z"/><path d="M9 23h14M9 26h14"/></svg>
    </header>
    <div class="section-text">
      <p>We will do our best to provide you with copies of everything we receive on your case. Most information will be emailed, <strong>so please keep your email address up to date.</strong></p>
    </div>
    <div class="photo" role="img" aria-label="Photo of a lawyer handing documents to a client beside law books and scales of justice" style="background:linear-gradient(135deg,#ecebe8,#b3aa9c 50%,#3b3a3c)"></div>
    <div class="rule"></div>
  </section>

  <section class="panel contact-info">
    <header class="section-head">
      <h2 class="section-title">Changes in Contact Information</h2>
      <svg class="section-icon" viewBox="0 0 32 32" fill="none" stroke="#fff" stroke-width="1"><path d="M6 8c-3 2-2 9 4 15s13 7 15 4l-4-5-3 2c-2-1-5-4-6-6l2-3z"/><path d="M17 3h12v9h-6l-3 3v-3h-3z"/><circle cx="20" cy="7.5" r="0.5"/><circle cx="23" cy="7.5" r="0.5"/><circle cx="26" cy="7.5" r="0.5"/></svg>
    </header>
    <div class="section-text">
      <p>If you move or change numbers during the case, please let us know. <strong>It is difficult to help if we are unable to reach you, and helping you is why we are here.</strong></p>
    </div>
    <div class="photo" role="img" aria-label="Photo of a client reviewing papers with an attorney" style="background:linear-gradient(135deg,#2f3b48,#7d8794 50%,#e3e2df)"></div>
    <div class="rule"></div>
  </section>

  <section class="panel court">
    <header class="section-head">
      <h2 class="section-title">Court Appearances</h2>
      <svg class="section-icon" viewBox="0 0 32 32" fill="none" stroke="#fff" stroke-width="1"><path d="M3 10L16 3l13 7z"/><path d="M4 10h24M5 28h22M3 30h26M7 12v14M25 12v14"/><circle cx="16" cy="7" r="1.5"/><path d="M16 13v11M11 15h10M11 15l-2 5h4zM21 15l-2 5h4zM13 24h6"/></svg>
    </header>
    <div class="section-text">
      <p>Cases do not get resolved as quickly as they do on television. Expect there to be several hearings in your case and it may be necessary for you to attend one or more of them. <strong>If a hearing is set, you will receive notice of the date and time of each hearing.</strong></p>
    </div>
    <div class="photo" role="img" aria-label="Photo of a lawyer addressing a jury seated in a wood-panelled courtroom" style="background:linear-gradient(180deg,#d8d5d0,#7a4d2e 40%,#5a3520)"></div>
    <div class="rule"></div>
  </section>

  <section class="panel billing">
    <header class="section-head">
      <h2 class="section-title">Billing and Collections</h2>
      <svg class="section-icon" viewBox="0 0 32 32" fill="none" stroke="#fff" stroke-width="1"><path d="M7 7h14v20c0 2-1 3-3 3H4c2 0 3-1 3-3z"/><path d="M10 12h8M10 16h8M10 20h8M10 24h5"/><circle cx="24" cy="8" r="6"/><path d="M26 6c-1-1-4-1-4 1s4 1 4 3-3 2-4 1M24 4v8"/></svg>
    </header>
    <div class="section-text">
      <p>We understand that this investment was a huge decision for you. As we focus on providing the best representation, <strong>we will need for you to stay on schedule with any payment arrangements agreed to at the time of your initial consultation.</strong></p>
    </div>
    <div class="photo" role="img" aria-label="Photo of a man reviewing an invoice on a desktop computer" style="background:linear-gradient(135deg,#f2f2f2,#c7c7c9 50%,#4a4038)"></div>
    <div class="rule"></div>
  </section>

  <section class="panel closing">
    <div class="quote-mark" style="top:40px">“</div>
    <p class="quote-text">Again, thank you for your trust in us.<br>We look forward to getting a<br>fantastic outcome on your case.</p>
    <div class="quote-mark" style="top:98px">“</div>
    <div class="contacts">
      <div class="contact" style="left:54px">
        <span class="contact-dot"><svg width="7" height="7" viewBox="0 0 10 10"><path d="M2 1c-1.5 1-1 4 1.5 6.5S8.5 10 9 8.5L7.5 6.5 6.2 7.3C5.3 6.8 3.6 5.1 3.1 4.2L3.9 2.9z" fill="none" stroke="var(--navy)" stroke-width="0.8"/></svg></span>
        (555) 014-2290
      </div>
      <div class="contact" style="left:123px">
        <span class="contact-dot"><svg width="7" height="7" viewBox="0 0 10 10" fill="none" stroke="var(--navy)" stroke-width="0.7"><circle cx="5" cy="5" r="4"/><ellipse cx="5" cy="5" rx="1.8" ry="4"/><path d="M1 5h8M1.6 3h6.8M1.6 7h6.8"/></svg></span>
        norwelllegalgroup.com
      </div>
      <div class="contact" style="left:210px">
        <span class="contact-dot"><svg width="7" height="7" viewBox="0 0 10 10" fill="none" stroke="var(--navy)" stroke-width="0.8"><rect x="1" y="2.2" width="8" height="5.6"/><path d="M1 2.2l4 3.3 4-3.3"/></svg></span>
        info@norwelllegalgroup.com
      </div>
    </div>
  </section>

</main>
</body>
</html>
```